Brisk. Technology Logistics Software platform.

A modern looking and feeling website for a logistics software platform.
We connect retailers or wholesale parcel distributors to worldwide delivery solutions.
Methods tend to be road and air transport to final mile courier companies and post offices all over the world.
Our platform is for ecommerce distribution. A customer uses BRISK to enable them to connect to worldwide companies who will track and trace the delivery of their goods.

Target Market(s)

Onllne retailers. Markert Places such as Tolvaro and Quendix. Wholesale third party logistics and packaging companies. Delivery companies based in the UK looking to expand overseas.

Number of Pages Required

5+ page

Font styles to use
Sans Serif

Colors
aaaaaa
dbdbdb
e6e6e6
c4c4c4
cbcbcb
c9c9c9
ec1f27
3176b5
0355a3

Requirements
Must have
• Landing Page.
• What we do.
• Who we are.
• Modules.
• Testimonies (password protected)
• Contact us.
• Interactive for mobile operating systems.
• Scrolling website.
• Short stock video showing on key pages.
• Very well polished fonts and buttons. A sharp and well executed website is required.
• Simplicity in feeling.
• To the point on message.
• Refined wording and copyrighting / messaging
• A link to our sub brand and product Brisk Parcels
• Capture interest so people read further.
Nice to have
• A polished video to explain what we do on landing page. Clipmarrow.net have some good options but not sure how professional they will look.
Should not have
• Bad graphics and colours.
• Not lots of clicks. Less as possible
• Complex message

```html
<!DOCTYPE html>
<html lang="en">
<head>
<meta charset="utf-8">
<title>Brisk. Technology</title>
<link href="https://fonts.googleapis.com/css2?family=Nunito:wght@400;600;700;800&display=swap" rel="stylesheet">
<style>
:root{
  --red:#ec1f27;
  --blue:#3176b5;
  --navy:#0355a3;
  --ink:#2a2a2a;
  --muted:#7a7a7a;
  --line:#dbdbdb;
  --soft:#c4c4c4;
  --page:#f6f6f6;
  --white:#ffffff;
}
*{box-sizing:border-box;margin:0;padding:0}
html,body{width:774px;height:1200px;overflow:hidden}
body{font-family:"Nunito",sans-serif;background:var(--page);color:var(--ink);position:relative}
.site-header{position:absolute;left:0;top:0;width:774px;height:62px;background:var(--white)}
.brand{position:absolute;left:100px;top:22px;font-size:18px;font-weight:800;color:var(--red);letter-spacing:.2px;white-space:nowrap}
.brand--footer{left:0;right:0;top:1018px;text-align:center;font-size:20px}
.contact-strip{position:absolute;top:12px;right:98px;display:flex;gap:16px;font-size:8px;color:var(--muted)}
.contact-strip span{display:flex;align-items:center;gap:5px}
.main-nav{position:absolute;top:37px;right:98px;display:flex;gap:28px;font-size:10px;font-weight:600}
.main-nav a,.footer-nav a{color:var(--ink);text-decoration:none}
.main-nav .is-active,.footer-nav .is-active{color:var(--blue)}
.hero{position:absolute;left:0;top:62px;width:774px;height:286px;background:linear-gradient(90deg,#6f7a84 0%,#9aa2a8 35%,#7d8891 60%,#4f6b8c 100%)}
.hero::after{content:"";position:absolute;inset:0;background:linear-gradient(180deg,rgba(40,50,60,.25),rgba(200,205,210,.15))}
.hero-title{position:absolute;left:0;right:0;top:106px;text-align:center;color:var(--white);font-size:20px;font-weight:800;line-height:25px;z-index:1}
.intro-panel{position:absolute;left:50px;top:348px;width:675px;height:159px;background:var(--white)}
.welcome{position:absolute;left:99px;top:400px;width:577px;height:249px;background:var(--red);color:var(--white);padding:42px 50px 0}
.welcome h2{font-size:24px;font-weight:600;display:flex;align-items:center;gap:14px}
.welcome h2::after{content:"";width:52px;height:1px;background:var(--white);display:block}
.welcome p{margin-top:19px;font-size:12px;line-height:16.8px;width:470px}
.btn{display:inline-block;margin-top:23px;background:var(--white);color:var(--red);font-size:10px;font-weight:600;padding:7px 15px;text-decoration:none}
.lead{position:absolute;left:0;right:0;top:686px;text-align:center;font-size:18.5px;line-height:22.5px;font-weight:400}
.features{position:absolute;left:99px;top:780px;display:flex;gap:18px}
.feature{width:180px}
.feature svg{display:block;height:34px}
.feature h3{margin-top:14px;font-size:13px;font-weight:600;color:var(--navy);border-left:1px solid var(--muted);padding-left:10px;line-height:14px}
.feature p{margin-top:12px;font-size:8.3px;line-height:12.5px;color:var(--muted)}
.site-footer{position:absolute;left:0;top:963px;width:774px;height:237px;background:var(--white)}
.footer-nav{position:absolute;left:0;right:0;top:1076px;display:flex;justify-content:center;gap:28px;font-size:10px;font-weight:600}
.social{position:absolute;left:0;right:0;top:1112px;display:flex;justify-content:center;gap:5px}
.social span{width:22px;height:22px;border-radius:50%;background:var(--soft)}
.social .is-hover{background:var(--red)}
.footer-rule{position:absolute;left:99px;top:1160px;width:577px;height:1px;background:var(--line)}
.copyright{position:absolute;left:0;right:0;top:1174px;text-align:center;font-size:8px;color:var(--ink)}
.copyright b{color:var(--red);font-weight:400}
</style>
</head>
<body>
<header class="site-header">
  <div class="brand">Brisk. Technology</div>
  <div class="contact-strip">
    <span><svg width="8" height="8" viewBox="0 0 10 10"><path d="M2 1l2 2-1 1.2c.6 1.2 1.6 2.2 2.8 2.8L7 6l2 2-1.3 1.3C4.5 9 1 5.5.7 2.3z" fill="#ec1f27"/></svg>123 - 456 - 7890</span>
    <span><svg width="9" height="7" viewBox="0 0 10 8"><rect width="10" height="8" rx="1" fill="#ec1f27"/><path d="M0 1l5 3.5L10 1" stroke="#fff" fill="none"/></svg>info@brisk.technology.com</span>
  </div>
  <nav class="main-nav">
    <a class="is-active" href="#">-- Home --</a><a href="#">Solutions</a><a href="#">Parcels</a><a href="#">Testimonials</a><a href="#">Contact Us</a>
  </nav>
</header>

<section class="hero" role="img" aria-label="Photo of a large industrial warehouse with heavy machinery">
  <h1 class="hero-title">We provide customised software<br>to manage your end to end e-commerce<br>delivery requirements</h1>
</section>

<div class="intro-panel"></div>
<section class="welcome">
  <h2>Welcome</h2>
  <p>With over 25 years of extensive experience within the UK and cross border Logistics Industry, our team have created a carrier management platform that can connect with your delivery providers, or work with over one hundred delivery solutions that are currently integrated into our system.</p>
  <a class="btn" href="#">Contact Us</a>
</section>

<h2 class="lead">This will provide you with a system that<br>we believe reflects the key factors of e-commerce<br>delivery today</h2>

<section class="features">
  <article class="feature">
    <svg width="34" height="32" viewBox="0 0 34 32" fill="none" stroke="#ec1f27" stroke-width="1.3"><rect x="1" y="1" width="32" height="30"/><line x1="1" y1="6" x2="33" y2="6"/><path d="M8 23a9 9 0 0 1 18 0"/><line x1="17" y1="23" x2="21" y2="17"/></svg>
    <h3>Velocity</h3>
    <p>We deliver IT projects on time, every time, allowing our clients to plan for their business needs effectively, and achieve fast time-to -market results.</p>
  </article>
  <article class="feature">
    <svg width="34" height="34" viewBox="0 0 34 34" fill="none" stroke="#ec1f27" stroke-width="1.3"><rect x="1" y="1" width="32" height="32"/><circle cx="17" cy="9" r="5"/><line x1="5" y1="32" x2="5" y2="24"/><line x1="9" y1="32" x2="9" y2="20"/><line x1="13" y1="32" x2="13" y2="26"/><rect x="19" y="19" width="12" height="13"/></svg>
    <h3>Accountability</h3>
    <p>Our systems provide clear audit trails from functionality including individual parcel booking through to supplier &amp; client invoice reconciliation</p>
  </article>
  <article class="feature">
    <svg width="32" height="34" viewBox="0 0 32 34" fill="none" stroke="#ec1f27" stroke-width="1.3"><rect x="3" y="1" width="12" height="6"/><path d="M9 8c-6 3-8 10-6 16h14c2-6 0-13-6-16z"/><circle cx="22" cy="24" r="7"/><circle cx="22" cy="24" r="3"/></svg>
    <h3>Cost reduction</h3>
    <p>With our non ‘label fee’ approach we provide low cost solutions that will help your business grow. There is no job too large or small and we constantly push the boundaries to optimise your processes.</p>
  </article>
</section>

<footer class="site-footer"></footer>
<div class="brand brand--footer">Brisk. Technology</div>
<nav class="footer-nav">
  <a class="is-active" href="#">-- Home --</a><a href="#">Solutions</a><a href="#">Parcels</a><a href="#">Testimonials</a><a href="#">Contact Us</a>
</nav>
<div class="social"><span></span><span class="is-hover"></span><span></span><span></span></div>
<div class="footer-rule"></div>
<p class="copyright">© 2019 <b>Brisk Technology.</b> All Rights Reserved. &nbsp;&nbsp; Terms &amp; Conditions &nbsp; I &nbsp; Privacy Policy</p>
</body>
</html>
```